Digital One Pager for Consulting Practice

I would like the essence of the content in my ppt consolidated into a one-pager. The one-pager will mainly be sent via email as a pdf and intended to excite and invite new clients and establish the credibility of my boutique high-end consulting firm. Infographics and symbols would be a plus. The target client should view the firm as providing premeir service. The client is getting a thought partner.

Target Market(s)

Large Medical Device Manufacturer Executives, Early-Stage Medical Device Manufacturer Executives, Partners at VC Firms

Industry/Entity Type

Medical Equipment

Colors
0355a3
f37122

Requirements
Must have
• Please match the color scheme in ppt. Please use the existing logo. I am very open to better graphics on the process. My photo does not need to be on the digital flyer. Hyper link to the website and email is needed.
Nice to have
• Infographics

```html
<!DOCTYPE html>
<html lang="en">
<head>
<meta charset="utf-8">
<title>Halden Ventures Value</title>
<link rel="stylesheet" href="https://fonts.googleapis.com/css2?family=Montserrat:wght@600&family=Open+Sans:wght@300;400;600&family=Tinos&display=swap">
<style>
  :root {
    --navy: #15223b;
    --navy-deep: #0f1a2e;
    --orange: #f37122;
    --red: #e84a2f;
    --slate: #34495c;
    --grey: #a6a8ab;
    --panel: #f1f1f1;
    --ink: #2b3546;
    --muted: #7b7f85;
    --white: #ffffff;
  }
  * { box-sizing: border-box; margin: 0; padding: 0; }
  html, body { width: 956px; height: 1200px; overflow: hidden; background: var(--white); }
  body { font-family: "Open Sans", Arial, sans-serif; color: var(--ink); position: relative; }

  .masthead {
    position: absolute; left: 0; top: 0; width: 956px; height: 430px;
    background: var(--navy); text-align: center; color: var(--white);
  }
  .brand {
    position: absolute; top: 70px; left: 0; width: 100%;
    display: flex; justify-content: center; align-items: center; gap: 18px;
  }
  .brand-dot { width: 46px; height: 46px; border-radius: 50%; background: var(--orange); }
  .brand-name {
    font-family: "Montserrat", Arial, sans-serif; font-weight: 600; color: var(--white);
    font-size: 44px; line-height: 1; letter-spacing: 4px; text-align: left;
  }
  .brand-name span { display: block; font-size: 30px; letter-spacing: 7px; margin-top: 6px; }
  .headline {
    position: absolute; top: 236px; width: 100%;
    font-family: "Tinos", "Times New Roman", serif; font-weight: 400;
    font-size: 56px; letter-spacing: 2px; color: var(--red);
  }
  .tagline {
    position: absolute; top: 322px; width: 100%;
    font-weight: 300; font-size: 28px; letter-spacing: .3px;
  }

  .services { position: absolute; left: 0; top: 430px; width: 478px; height: 690px; background: var(--white); }
  .services svg { position: absolute; left: 0; top: 0; }
  .hex-title { font-family: "Open Sans", Arial, sans-serif; font-size: 17px; fill: var(--white); text-anchor: middle; }
  .hex-sub { font-family: "Open Sans", Arial, sans-serif; font-size: 12.5px; fill: var(--white); text-anchor: middle; }

  .offer { position: absolute; left: 478px; top: 430px; width: 478px; height: 690px; background: var(--panel); padding: 62px 30px 0 40px; }
  .section-title { font-family: "Tinos", "Times New Roman", serif; font-weight: 400; color: var(--orange); font-size: 27px; }
  .group-title { font-weight: 600; font-size: 15.5px; color: var(--ink); margin-top: 12px; }
  .points { list-style: none; margin-top: 6px; }
  .points li { position: relative; padding-left: 28px; font-size: 15.5px; line-height: 1.35; color: var(--muted); margin-bottom: 10px; }
  .points li::before {
    content: ""; position: absolute; left: 2px; top: 4px; width: 12px; height: 12px;
    border: 1.4px solid var(--muted); border-radius: 50%;
  }
  .points li::after {
    content: ""; position: absolute; left: 6px; top: 8.5px; width: 3px; height: 3px;
    border-right: 1.4px solid var(--muted); border-top: 1.4px solid var(--muted); transform: rotate(45deg);
  }
  .group-title + .points { margin-bottom: 14px; }

  .process { display: flex; justify-content: space-between; margin-top: 18px; width: 390px; }
  .step { width: 96px; text-align: center; }
  .step-icon {
    width: 62px; height: 62px; margin: 0 auto; border-radius: 50%; background: var(--orange);
    box-shadow: 0 8px 6px -6px rgba(0,0,0,.25); display: flex; align-items: center; justify-content: center;
  }
  .step-label { font-size: 11px; line-height: 1.25; color: var(--muted); margin-top: 12px; letter-spacing: .3px; }

  .partners-title { font-weight: 600; font-size: 16px; color: var(--ink); margin-top: 30px; }
  .partners { display: flex; flex-wrap: wrap; gap: 10px 12px; margin-top: 8px; width: 400px; align-items: center; }
  .badge { height: 26px; border-radius: 3px; background: #c9cdd3; }
  .badge.dark { background: var(--navy); }
  .badge.blue { background: #2a63b0; }

  .footer { position: absolute; left: 0; top: 1120px; width: 956px; height: 80px; display: flex; }
  .footer-phone {
    width: 478px; background: var(--orange); color: var(--white);
    display: flex; align-items: center; justify-content: center; gap: 18px; font-size: 37px;
  }
  .footer-links {
    width: 478px; background: var(--navy-deep); color: var(--white);
    display: flex; align-items: center; justify-content: center; font-size: 17px;
  }
  .footer-links a { color: var(--white); text-decoration: none; }
  .footer-links .sep { margin: 0 10px; }
</style>
</head>
<body>

<header class="masthead">
  <div class="brand">
    <div class="brand-dot"></div>
    <div class="brand-name">HALDEN<span>VENTURES</span></div>
  </div>
  <h1 class="headline">HALDEN VENTURES VALUE</h1>
  <p class="tagline">Extensive Experience | Efficient Process | Valued Network</p>
</header>

<section class="services" aria-label="Services">
  <svg width="478" height="690" viewBox="0 0 478 690">
    <!-- Regulatory Strategy -->
    <g transform="translate(32,66)">
      <polygon points="63,0 189,0 252,105 189,210 63,210 0,105" fill="var(--orange)"/>
      <text class="hex-title" x="126" y="100">REGULATORY</text>
      <text class="hex-title" x="126" y="123">STRATEGY</text>
      <text class="hex-sub" x="126" y="146">RAQA Organizational Structure</text>
      <text class="hex-sub" x="126" y="164">Regulatory Pathway</text>
    </g>
    <!-- Interim Executive Leadership -->
    <g transform="translate(32,279)">
      <polygon points="63,0 189,0 252,105 189,210 63,210 0,105" fill="var(--grey)"/>
      <text class="hex-title" x="126" y="94">INTERIM</text>
      <text class="hex-title" x="126" y="117">EXECUTIVE LEADERSHIP</text>
      <text class="hex-sub" x="126" y="144">Compliance Remediation</text>
      <text class="hex-sub" x="126" y="162">Accelerated Product</text>
      <text class="hex-sub" x="126" y="180">Registration</text>
    </g>
    <!-- FDA Communications -->
    <g transform="translate(223,173)">
      <polygon points="63,0 189,0 252,105 189,210 63,210 0,105" fill="var(--red)"/>
      <text class="hex-title" x="126" y="100">FDA</text>
      <text class="hex-title" x="126" y="123">COMMUNICATIONS</text>
      <text class="hex-sub" x="126" y="146">Deficiency Response</text>
      <text class="hex-sub" x="126" y="164">Application Review</text>
    </g>
    <!-- Training -->
    <g transform="translate(223,385)">
      <polygon points="63,0 189,0 252,105 189,210 63,210 0,105" fill="var(--slate)"/>
      <text class="hex-title" x="126" y="108">TRAINING</text>
      <text class="hex-sub" x="126" y="136">FDA Communication</text>
      <text class="hex-sub" x="126" y="154">MDR Reporting</text>
    </g>

    <!-- icon: chart -->
    <g transform="translate(158,76)">
      <circle r="31" fill="var(--white)"/>
      <rect x="-15" y="2" width="6" height="12" fill="var(--orange)"/>
      <rect x="-6" y="-3" width="6" height="17" fill="var(--orange)"/>
      <rect x="3" y="-8" width="6" height="22" fill="var(--orange)"/>
      <rect x="12" y="-12" width="6" height="26" fill="var(--orange)"/>
      <polyline points="-17,-4 -4,-14 4,-9 16,-20" fill="none" stroke="var(--orange)" stroke-width="2.5"/>
    </g>
    <!-- icon: documents -->
    <g transform="translate(349,202)">
      <circle r="31" fill="var(--white)"/>
      <rect x="-12" y="-17" width="22" height="30" fill="none" stroke="var(--red)" stroke-width="2.5"/>
      <rect x="-6" y="-12" width="22" height="30" fill="var(--red)"/>
      <line x1="-1" y1="-4" x2="11" y2="-4" stroke="var(--white)" stroke-width="2"/>
      <line x1="-1" y1="2" x2="11" y2="2" stroke="var(--white)" stroke-width="2"/>
      <line x1="-1" y1="8" x2="11" y2="8" stroke="var(--white)" stroke-width="2"/>
    </g>
    <!-- icon: leader network -->
    <g transform="translate(158,298)">
      <circle r="31" fill="var(--white)"/>
      <circle cy="-10" r="7" fill="var(--grey)"/>
      <path d="M-11 8 Q0 -4 11 8 Z" fill="var(--grey)"/>
      <line x1="0" y1="8" x2="0" y2="16" stroke="var(--grey)" stroke-width="2"/>
      <line x1="-16" y1="16" x2="16" y2="16" stroke="var(--grey)" stroke-width="2"/>
      <circle cx="-16" cy="16" r="3" fill="var(--grey)"/>
      <circle cx="0" cy="16" r="3" fill="var(--grey)"/>
      <circle cx="16" cy="16" r="3" fill="var(--grey)"/>
    </g>
    <!-- icon: clipboard -->
    <g transform="translate(349,404)">
      <circle r="31" fill="var(--white)"/>
      <rect x="-12" y="-16" width="24" height="32" rx="2" fill="none" stroke="var(--slate)" stroke-width="2.5"/>
      <line x1="-6" y1="-7" x2="6" y2="-7" stroke="var(--slate)" stroke-width="2"/>
      <line x1="-6" y1="-1" x2="6" y2="-1" stroke="var(--slate)" stroke-width="2"/>
      <line x1="-6" y1="5" x2="2" y2="5" stroke="var(--slate)" stroke-width="2"/>
      <line x1="4" y1="14" x2="16" y2="-4" stroke="var(--slate)" stroke-width="3"/>
    </g>
  </svg>
</section>

<section class="offer">
  <h2 class="section-title">Experience to Provide...</h2>
  <h3 class="group-title">Executive Application Review</h3>
  <ul class="points">
    <li>Examples include: Presubmission, IDE, 510(k), 513(g), PMA, Refuse to Accept, Hold letter</li>
    <li>Troubleshooting</li>
  </ul>
  <h3 class="group-title">Strategic Advice &amp; Diligence to Investors</h3>
  <ul class="points">
    <li>Validate &amp; Verify Founder Milestones</li>
    <li>Diligence portfolio company Regulatory and Quality systems</li>
  </ul>

  <h2 class="section-title">Efficient Process</h2>
  <div class="process">
    <div class="step">
      <div class="step-icon">
        <svg width="34" height="34" viewBox="0 0 34 34" aria-hidden="true"><circle cx="17" cy="12" r="7" fill="#fff"/><path d="M5 32 Q17 16 29 32 Z" fill="#fff"/><path d="M8 13 Q8 3 17 3 Q26 3 26 13" fill="none" stroke="#fff" stroke-width="2"/></svg>
      </div>
      <div class="step-label">EXPLORATORY<br>CALL</div>
    </div>
    <div class="step">
      <div class="step-icon">
        <svg width="34" height="34" viewBox="0 0 34 34" aria-hidden="true"><rect x="5" y="3" width="18" height="24" fill="none" stroke="#fff" stroke-width="2.2"/><line x1="9" y1="10" x2="19" y2="10" stroke="#fff" stroke-width="2"/><line x1="9" y1="15" x2="16" y2="15" stroke="#fff" stroke-width="2"/><circle cx="22" cy="22" r="5" fill="none" stroke="#fff" stroke-width="2.2"/><line x1="26" y1="26" x2="31" y2="31" stroke="#fff" stroke-width="2.6"/></svg>
      </div>
      <div class="step-label">REGULATORY<br>LANDSCAPE</div>
    </div>
    <div class="step">
      <div class="step-icon">
        <svg width="34" height="34" viewBox="0 0 34 34" aria-hidden="true"><circle cx="17" cy="13" r="9" fill="#fff"/><rect x="12" y="21" width="10" height="5" fill="#fff"/><rect x="13" y="27" width="8" height="3" rx="1" fill="#fff"/></svg>
      </div>
      <div class="step-label">PROBLEM<br>STATEMENT</div>
    </div>
    <div class="step">
      <div class="step-icon">
        <svg width="34" height="34" viewBox="0 0 34 34" aria-hidden="true"><circle cx="13" cy="20" r="7" fill="none" stroke="#fff" stroke-width="4" stroke-dasharray="3 2.5"/><circle cx="13" cy="20" r="3" fill="#fff"/><circle cx="24" cy="10" r="5" fill="none" stroke="#fff" stroke-width="3" stroke-dasharray="2.5 2"/></svg>
      </div>
      <div class="step-label">REVIEW &amp; ALIGN<br>ON DELIVERABLES</div>
    </div>
  </div>

  <h3 class="partners-title">Valued Partner Network</h3>
  <div class="partners" aria-label="Partner badges">
    <div class="badge" style="width:240px"></div>
    <div class="badge" style="width:58px"></div>
    <div class="badge dark" style="width:62px;height:30px"></div>
    <div class="badge" style="width:64px"></div>
    <div class="badge blue" style="width:52px"></div>
    <div class="badge" style="width:44px"></div>
  </div>
</section>

<footer class="footer">
  <div class="footer-phone">
    <svg width="30" height="30" viewBox="0 0 30 30" aria-hidden="true"><circle cx="15" cy="15" r="13" fill="none" stroke="#fff" stroke-width="2"/><path d="M10 8 L13 8 L14 12 L12 13.5 Q14 17 16.5 18 L18 16 L22 17 L22 20 Q18 22 14 19 Q9 15 10 8 Z" fill="#fff"/></svg>
    <span>555.014.2290</span>
  </div>
  <div class="footer-links">
    <a href="https://www.haldenventures.com">www.haldenventures.com</a>
    <span class="sep">|</span>
    <a href="mailto:info@haldenventures.com">info@haldenventures.com</a>
  </div>
</footer>

</body>
</html>
```